Initial website for sport tech startup

We are currently in the R&D phases of our new product. It’s a headband to prevent concussion in the soccer market initially.

We have 2 products, one that’s basic aimed at the youth market and the other more technology driven that’s aimed at the academies and professional market.

Initially the product will launch in the UK

Target Market(s)

Youth soccer players and parents in UK, Soccer Clubs, Federations.

Industry/Entity Type

Sporting Good

Coding

Coded - Design and coding required

Number of Pages Required

5+ page

Requirements
Must have
• Professional style that can be adapted and changed over the coming months.
Nice to have
• Ecommerce ability in the future.

```html
<!DOCTYPE html>
<html lang="en">
<head>
<meta charset="utf-8">
<title>Cranvel – Bringing Safety to the Sports Concussion Debate</title>
<link href="https://fonts.googleapis.com/css2?family=Poppins:wght@300;400;500;600;700;800&display=swap" rel="stylesheet">
<style>
:root{
  --sky:#00a2e6;
  --sky-bright:#00aeef;
  --navy:#0a6391;
  --ink:#1c1c1c;
  --body:#333a40;
  --muted:#7b8a96;
  --pale:#eef2f6;
  --blog-bg:#f4f6f8;
  --footer:#2b2b2b;
  --footer-text:#a5a5a5;
  --white:#ffffff;
}
*{box-sizing:border-box;margin:0;padding:0}
html,body{width:1200px;height:3337px;overflow:hidden}
body{font-family:'Poppins',sans-serif;color:var(--body);background:var(--white);position:relative}
a{color:inherit;text-decoration:none}
h1,h2,h3,h4,h5{font-weight:inherit}

/* Hero */
.hero{position:absolute;left:0;top:0;width:1200px;height:595px;background:var(--pale);overflow:hidden}
.hero-blue{position:absolute;inset:0;background:var(--sky);clip-path:polygon(0 0,647px 0,647px 265px,522px 265px,522px 595px,0 595px)}
.hero-strip{position:absolute;left:647px;top:0;width:27px;height:265px;background:var(--white)}
.hero-strip-low{position:absolute;left:522px;top:265px;width:27px;height:330px;background:var(--white)}
.logo{position:absolute;font-family:'Poppins',sans-serif;font-weight:500;letter-spacing:1px;color:var(--white)}
.hero .logo{left:118px;top:36px;font-size:32px}
.nav{position:absolute;left:692px;top:40px;width:333px;height:40px;background:var(--white);border-radius:20px;display:flex;align-items:center;gap:32px;padding-left:36px;font-size:13px;color:#6b7680}
.nav .active{color:var(--ink);font-weight:500;position:relative}
.nav .active::after{content:"";position:absolute;left:50%;bottom:-8px;width:3px;height:3px;border-radius:50%;background:var(--ink)}
.cart{position:absolute;left:1049px;top:50px}
.cart-count{position:absolute;left:1066px;top:41px;width:16px;height:16px;border-radius:50%;background:var(--sky-bright);color:var(--white);font-size:10px;text-align:center;line-height:16px}
.hero-title{position:absolute;left:118px;top:205px;color:var(--white);font-weight:800;font-size:38px;line-height:48px;text-transform:uppercase}
.hero-title span{color:var(--ink);display:block}
.btn-outline-light{position:absolute;left:118px;top:442px;width:139px;height:40px;border:2px solid var(--white);border-radius:20px;color:var(--white);font-size:13px;font-weight:500;text-align:center;line-height:36px}
.hero-visual{position:absolute;left:530px;top:115px;width:535px;height:410px;background:linear-gradient(150deg,#8a929c,#5c6570 55%,#e48a3a)}

/* About */
.about-title{position:absolute;left:120px;top:700px;width:480px;font-size:23.5px;font-weight:600;line-height:37px;color:var(--ink);text-transform:uppercase}
.about-text{position:absolute;left:120px;top:800px;width:480px;font-size:15.5px;letter-spacing:-0.3px;line-height:30px;color:var(--ink)}
.about-text p+p{margin-top:16px}
.photo-frame-lg{position:absolute;left:670px;top:680px;width:359px;height:340px;border:2px solid var(--navy)}
.photo-lg{position:absolute;left:683px;top:695px;width:334px;height:312px;background:linear-gradient(135deg,#5b6f88,#b8c0c8 55%,#7d8a70)}
.photo-frame-sm{position:absolute;left:622px;top:907px;width:215px;height:152px;border:2px solid var(--navy);background:#dfe7ee}
.photo-sm{position:absolute;left:631px;top:915px;width:198px;height:135px;background:linear-gradient(180deg,#8a9ba8,#4d7a3e)}

/* Product info */
.product-info{position:absolute;left:0;top:1153px;width:1200px;height:525px;background:var(--navy)}
.section-title-light{position:absolute;left:0;top:70px;width:1200px;text-align:center;color:var(--white);font-size:30px;font-weight:300}
.section-title-light b{font-weight:700}
.feature-card{position:absolute;top:151px;width:223px;height:251px;background:var(--white);border:1px solid #cfe6b8;text-align:center;padding-top:34px}
.feature-card.raised{top:155px;padding-top:26px}
.feature-card svg{display:block;margin:0 auto}
.feature-card h3{margin-top:26px;font-size:16px;font-weight:600;color:var(--ink)}
.feature-card.raised h3{margin-top:16px}
.feature-card p{margin:18px auto 0;width:150px;font-size:13px;line-height:22px;color:var(--muted)}
.feature-card .go{display:block;margin:16px auto 0;width:32px;height:32px;border-radius:50%;background:var(--navy)}

/* Headband */
.headband-title{position:absolute;left:0;top:1734px;width:1200px;text-align:center;font-size:31px;font-weight:700;color:var(--ink)}
.headband-rule{position:absolute;left:597px;top:1782px;width:1px;height:26px;background:#999}
.headband-visual{position:absolute;left:340px;top:1835px;width:502px;height:285px;background:linear-gradient(160deg,#6a727d,#4a525d)}
.btn-primary{position:absolute;left:531px;top:2131px;width:138px;height:36px;border-radius:18px;background:var(--sky-bright);color:var(--white);font-size:13px;font-weight:500;text-align:center;line-height:36px}
.dots{position:absolute;left:575px;top:2213px;display:flex;gap:9px}
.dots i{width:10px;height:10px;border-radius:50%;background:#c4ccd3}
.dots i.on{background:var(--navy)}

/* Blog */
.blog{position:absolute;left:0;top:2278px;width:1200px;height:592px;background:var(--blog-bg)}
.blog-title{position:absolute;left:0;top:46px;width:1200px;text-align:center;font-size:40px;font-weight:300;color:var(--navy)}
.blog-title b{font-weight:700;color:var(--ink)}
.blog-sub{position:absolute;left:0;top:105px;width:1200px;text-align:center;font-size:19px;font-weight:300;color:var(--muted)}
.blog-image{position:absolute;top:167px;width:411px;height:245px}
.blog-image.keeper{left:146px;background:linear-gradient(135deg,#3a4a5c,#9aa4ae 60%,#2a3440)}
.blog-image.ball{left:618px;background:linear-gradient(180deg,#c9cfc6,#6f7b58 70%,#3c4a2e)}
.blog-card{position:absolute;top:356px;width:288px;height:89px;background:var(--white);box-shadow:0 4px 14px rgba(0,0,0,.06);padding:14px 18px}
.blog-card h4{font-size:10.5px;font-weight:500;line-height:19px;color:#2b3a55;width:210px}
.blog-card .tag{margin-top:4px;font-size:12px;color:var(--muted);display:flex;align-items:center;gap:12px}
.blog-card .tag::before{content:"";width:26px;height:2px;background:#5bbf6a}
.blog-card.grey .tag::before{background:#b5bcc2}
.blog-card .arrow{position:absolute;right:18px;top:30px;width:30px;height:30px;border:1px solid #d9dee2;border-radius:50%}
.blog-card .arrow svg{display:block}
.btn-outline{position:absolute;left:520px;top:486px;width:160px;height:36px;border:2px solid #8b969f;border-radius:18px;text-align:center;line-height:32px;font-size:13px;font-weight:500;color:var(--ink)}

/* Newsletter */
.newsletter-title{position:absolute;left:0;top:2920px;width:1200px;text-align:center;font-size:31px;font-weight:400;color:var(--ink)}
.newsletter-field{position:absolute;left:259px;top:3002px;width:677px;height:25px;border-bottom:1px solid #cfd5da;font-size:10px;color:#a9b1b8;display:flex;justify-content:space-between}

/* Footer */
.footer{position:absolute;left:0;top:3087px;width:1200px;height:250px;background:var(--footer);color:var(--footer-text);font-size:13px}
.footer h5{font-size:15px;font-weight:400;color:#e4e4e4}
.footer-col{position:absolute;top:45px}
.footer-col p{line-height:22px;margin-top:18px}
.footer-col ul{list-style:none;margin-top:16px}
.footer-col li{line-height:28px}
.footer-divider{position:absolute;top:48px;width:1px;height:140px;background:#3d3d3d}
.footer .logo{left:850px;top:73px;font-size:30px;color:var(--white)}
.social{position:absolute;left:870px;top:143px;display:flex;gap:14px}
.social i{width:14px;height:14px;border:1.5px solid #9a9a9a;border-radius:50%}
</style>
</head>
<body>

<header class="hero">
  <div class="hero-blue"></div>
  <div class="hero-strip"></div>
  <div class="hero-strip-low"></div>
  <div class="logo">CRANVEL</div>
  <nav class="nav">
    <a class="active" href="#">Home</a><a href="#">Products</a><a href="#">Shop</a><a href="#">Contact</a>
  </nav>
  <svg class="cart" width="26" height="24" viewBox="0 0 26 24" fill="none" stroke="#6b7680" stroke-width="1.6"><path d="M1 2h4l3 13h13l3-9H7"/><circle cx="10" cy="20" r="1.8"/><circle cx="19" cy="20" r="1.8"/></svg>
  <div class="cart-count">0</div>
  <h1 class="hero-title">Bringing Safety<br>to the Sports<span>Concussion</span><span>Debate</span></h1>
  <a class="btn-outline-light" href="#">Learn More</a>
  <div class="hero-visual" role="img" aria-label="Protective headband product illustration with scattered orange triangles"></div>
</header>

<section>
  <h2 class="about-title">Cranvel – Bringing safety to the sports concussion debate</h2>
  <div class="about-text">
    <p>Cranvel is designing and developing head protectioCranvel protection products to reduce the likelihood of concussion when playing sports.</p>
    <p>Exploring and understanding medical insights, material science and composites research, current and former players experiences and governing bodies guidelines has allowed Cranvel to develop the safety</p>
  </div>
  <div class="photo-frame-lg"></div>
  <div class="photo-lg" role="img" aria-label="Two soccer players heading the ball"></div>
  <div class="photo-frame-sm"></div>
  <div class="photo-sm" role="img" aria-label="Injured player being attended on the pitch"></div>
</section>

<section class="product-info">
  <h2 class="section-title-light">Product <b>Info</b></h2>
  <div class="feature-card" style="left:240px">
    <svg width="48" height="50" viewBox="0 0 48 50" fill="none" stroke="#0a6391" stroke-width="1.6"><rect x="8" y="2" width="34" height="42" rx="3"/><path d="M14 10h22M14 16h22M14 22h16"/><path d="M4 36l6 7 12-14"/></svg>
    <h3>Safety Tested</h3>
    <p>Lorem Ipsum is simply dummy text of the</p>
  </div>
  <div class="feature-card raised" style="left:489px">
    <svg width="52" height="48" viewBox="0 0 52 48" fill="none" stroke="#0a6391" stroke-width="1.6"><path d="M8 32C14 14 30 6 46 4 42 20 30 30 12 32z"/><path d="M8 32L34 14"/><path d="M2 44h48"/></svg>
    <h3>Light Weight</h3>
    <p>Lorem Ipsum is simply dummy text of the</p>
    <span class="go"><svg width="32" height="32" viewBox="0 0 32 32" fill="none" stroke="#fff" stroke-width="1.6"><path d="M10 16h12M17 11l5 5-5 5"/></svg></span>
  </div>
  <div class="feature-card" style="left:737px">
    <svg width="54" height="50" viewBox="0 0 54 50" fill="none" stroke="#0a6391" stroke-width="1.6"><rect x="10" y="8" width="28" height="26" rx="8"/><path d="M4 28h40v10H4zM8 38v6M40 38v6M48 4v40M44 4h8"/></svg>
    <h3>Comfortable</h3>
    <p>Lorem Ipsum is simply dummy text of the</p>
  </div>
</section>

<section>
  <h2 class="headband-title">Headband</h2>
  <div class="headband-rule"></div>
  <div class="headband-visual" role="img" aria-label="Cranvel protective headband product"></div>
  <a class="btn-primary" href="#">Shop Now</a>
  <div class="dots"><i></i><i class="on"></i><i></i></div>
</section>

<section class="blog">
  <h2 class="blog-title">Our <b>Blog</b></h2>
  <p class="blog-sub">Lorem Ipsum is simply dummy text of the printing</p>
  <div class="blog-image keeper" role="img" aria-label="Goalkeeper diving to catch the ball"></div>
  <div class="blog-card" style="left:293px">
    <h4>Lorem Ipsum is simply dummy text of the printing and typesetting</h4>
    <div class="tag">Headband</div>
    <span class="arrow"><svg width="28" height="28" viewBox="0 0 28 28" fill="none" stroke="#5bbf6a" stroke-width="1.5"><path d="M12 10l4 4-4 4"/></svg></span>
  </div>
  <div class="blog-image ball" role="img" aria-label="Player's boot resting on a soccer ball in a stadium"></div>
  <div class="blog-card grey" style="left:765px">
    <h4>Lorem Ipsum is simply dummy text of the printing and typesetting</h4>
    <div class="tag">Headband</div>
    <span class="arrow"><svg width="28" height="28" viewBox="0 0 28 28" fill="none" stroke="#b5bcc2" stroke-width="1.5"><path d="M12 10l4 4-4 4"/></svg></span>
  </div>
  <a class="btn-outline" href="#">View More</a>
</section>

<section>
  <h2 class="newsletter-title">Join Our Newsletter</h2>
  <div class="newsletter-field"><span>Your email address</span><span>Subscribe</span></div>
</section>

<footer class="footer">
  <div class="footer-col" style="left:153px">
    <h5>Contact Us</h5>
    <p>Lorem Ipsum, is simply<br>dummy text of the</p>
    <p>+xxx xxxx xxxxx</p>
    <p style="margin-top:10px">xxxxxxx@mailbox.test</p>
  </div>
  <div class="footer-divider" style="left:403px"></div>
  <div class="footer-col" style="left:530px">
    <h5>Contact Us</h5>
    <ul><li>Home</li><li>About</li><li>Shop</li><li>Contact</li></ul>
  </div>
  <div class="footer-divider" style="left:733px"></div>
  <div class="logo">CRANVEL</div>
  <div class="social"><i></i><i></i><i></i><i></i><i></i></div>
</footer>

</body>
</html>
```